Business cards for Paperleaf Sprites

Please note that the color of the logo has been changed from green to teal blue. Sorry for the changing!

Anything will go but want to have some funky side.

I would like the front of the business card is the logo and business information and the back side is the Adult Coloring, so that would attract the customer to do the coloring on the other side. Have more interactive side. (pictures for references only can see it below). Fairies on the back of the card for coloring and whatever you want to adds on to color, like flowers, nature etc......

Scrapbooking is not just paper, it also involves watercolor, mixed media, art, all the fun stuff.

Another keypoint I would like to stress on is the back of the business card should be Adult Coloring and make sure you are not google and use the search engine to copy and paste because of the copyright issue.

As a designer, I am sure you all can create beautiful artwork.

Please submit your creativities!

Want the business card is out of the ordinary and customers would like to keep that as a keepsake rather than treat like a regular business card and trash it. Fonts cannot be too small, consider some of the customers have to wear bi-focal eyeglasses.

Thanks a lot!

Target Market(s)

Scrapbooking, Card making, papercraft, stampin‘ , gifts items , etc.

Industry/Entity Type

Retail

Contact Information for Business Card

Color Scheme, please match with the Logo. Watercolor effect is nice!
Thanks!

Font styles to use
Serif

Requirements
Must have
• I would like Elegant and playful.
• Thanks!
Nice to have
• Watercolor effect or check out the Adult Coloring Book, I am thinking we can use a double-sided business card, one side for the information and the other side for people can do the coloring. I have attached 2 pictures for reference.
Should not have
• No black color on the background please!

```html
<!DOCTYPE html>
<html lang="en">
<head>
<meta charset="utf-8">
<title>Paperleaf Sprites – Business Cards</title>
<link rel="stylesheet" href="https://fonts.googleapis.com/css2?family=Lora:wght@400;600;700&display=swap">
<style>
  :root {
    --page-bg: #eceae4;
    --teal: #1f8088;
    --teal-soft: #5fa9ae;
    --deep-teal: #17686f;
    --paper-white: #ffffff;
    --ornament-tone: #d3e8e9;
    --card-shadow: rgba(40, 50, 50, 0.2);
  }
  html, body {
    margin: 0;
    width: 1200px;
    height: 900px;
    overflow: hidden;
    background: var(--page-bg);
    font-family: "Lora", Georgia, serif;
  }
  .canvas {
    position: relative;
    width: 1200px;
    height: 900px;
  }
  .card {
    position: absolute;
    width: 560px;
    height: 320px;
    box-shadow: 0 10px 24px var(--card-shadow);
  }
  .card svg { display: block; }
  .card--back { left: 70px; top: 120px; }
  .card--front { left: 570px; top: 460px; }
  .brand-name {
    font-family: "Lora", Georgia, serif;
    font-weight: 700;
    fill: var(--deep-teal);
  }
  .contact-name { font-family: "Lora", Georgia, serif; font-weight: 700; fill: var(--paper-white); }
  .contact-text { font-family: "Lora", Georgia, serif; font-weight: 400; fill: var(--paper-white); }
</style>
</head>
<body>
<main class="canvas">

  <!-- Back of card: coloring-art field, white band and circle with the name -->
  <section class="card card--back" aria-label="Business card, back side">
    <svg width="560" height="320" viewBox="0 0 560 320">
      <defs>
        <linearGradient id="coloringWash" x1="0" y1="0" x2="1" y2="1">
          <stop offset="0" stop-color="var(--teal)"/>
          <stop offset="1" stop-color="var(--teal-soft)"/>
        </linearGradient>
      </defs>
      <rect class="coloring-art" width="560" height="320" fill="url(#coloringWash)"
            role="img" aria-label="Adult-coloring line art of fairies, flowers and leaves for customers to color in"/>
      <rect class="back-band" x="0" y="92" width="560" height="96" fill="var(--paper-white)"/>
      <circle class="back-circle" cx="280" cy="140" r="118" fill="var(--paper-white)"/>

      <g class="flourish" role="img" aria-label="Small leaf flourish ornaments around the band">
        <ellipse cx="140" cy="74" rx="20" ry="8" fill="var(--ornament-tone)"/>
        <ellipse cx="422" cy="74" rx="20" ry="8" fill="var(--ornament-tone)"/>
        <ellipse cx="140" cy="206" rx="20" ry="8" fill="var(--ornament-tone)"/>
        <ellipse cx="422" cy="206" rx="20" ry="8" fill="var(--ornament-tone)"/>
      </g>

      <text class="brand-name" x="280" y="152" font-size="36" text-anchor="middle">Paperleaf Sprites</text>
    </svg>
  </section>

  <!-- Front of card: name mark and contact details -->
  <section class="card card--front" aria-label="Business card, front side">
    <svg width="560" height="320" viewBox="0 0 560 320">
      <rect class="front-top" width="560" height="320" fill="var(--paper-white)"/>
      <path class="front-base" d="M0,150 H130 A150,40 0 0 0 430,150 H560 V320 H0 Z" fill="var(--deep-teal)"/>

      <text class="brand-name" x="280" y="112" font-size="36" text-anchor="middle">Paperleaf Sprites</text>

      <text class="contact-name" x="252" y="236" font-size="18" text-anchor="end">Daniel Hartley</text>
      <text class="contact-text" x="252" y="256" font-size="14" text-anchor="end">Managing Director</text>

      <line class="divider" x1="266" y1="208" x2="266" y2="266" stroke="var(--paper-white)" stroke-width="1.2"/>

      <g class="contact-list">
        <!-- phone -->
        <path d="M280,213 q1,-2 3,-1 l2,2 q1,1 0,2 l-1,1 q1,2 3,3 l1,-1 q1,-1 2,0 l2,2 q1,2 -1,3 q-4,1 -8,-3 q-4,-4 -3,-8z" fill="var(--paper-white)"/>
        <text class="contact-text" x="298" y="223" font-size="13">(044)123456789</text>
        <!-- mail -->
        <rect x="280" y="234" width="11" height="8" fill="var(--paper-white)"/>
        <path d="M280,234 l5.5,4.5 l5.5,-4.5" fill="none" stroke="var(--deep-teal)" stroke-width="1"/>
        <text class="contact-text" x="298" y="243" font-size="13">info@youremail.com</text>
        <!-- web -->
        <circle cx="285.5" cy="258.5" r="5.5" fill="var(--paper-white)"/>
        <text class="contact-text" x="298" y="263" font-size="13">www.yourwebsite.com</text>
      </g>

      <text class="contact-text" x="96" y="298" font-size="15">1234, Address GoesHere, Country name , 12345</text>
    </svg>
  </section>

</main>
</body>
</html>
```